PLM - Business Card Design Project

We need a business card based on our logo
Updates

Hi I just upload logo file in AI format Thanks and regards

Target Market(s)

Bank, Big companies, Business owners

Industry/Entity Type

Business

Font styles to use
Sans Serif

```html
<!DOCTYPE html>
<html lang="fr">
<head>
<meta charset="utf-8">
<title>PLM – Carte de visite</title>
<link rel="stylesheet" href="https://fonts.googleapis.com/css2?family=Open+Sans:wght@300;400;700&display=swap">
<style>
  :root {
    --backdrop: #7f9193;
    --card-white: #ffffff;
    --navy: #112a4e;
    --navy-light: #4d6283;
    --slate: #869a9b;
    --logo-sub: #5f6f84;
    --text-dark: #132a4c;
  }
  * { margin: 0; padding: 0; box-sizing: border-box; }
  html, body {
    width: 1200px;
    height: 900px;
    overflow: hidden;
    background: var(--backdrop);
    font-family: "Open Sans", Arial, sans-serif;
  }
  .business-card {
    position: absolute;
    left: 160px;
    top: 200px;
    width: 880px;
    height: 500px;
    background: var(--card-white);
    overflow: hidden;
    box-shadow: 0 14px 34px rgba(0, 0, 0, 0.28);
  }
  .wave-band {
    position: absolute;
    inset: 0;
    width: 880px;
    height: 500px;
  }
  .brand {
    position: absolute;
    left: 88px;
    top: 128px;
    color: var(--navy);
  }
  .brand-name {
    display: block;
    font-weight: 300;
    font-size: 120px;
    line-height: 1;
    letter-spacing: 4px;
  }
  .brand-firm {
    display: block;
    margin-top: 6px;
    font-weight: 300;
    font-size: 23px;
    color: var(--logo-sub);
    letter-spacing: 0.5px;
  }
  .divider {
    position: absolute;
    left: 545px;
    top: 70px;
    width: 2px;
    height: 190px;
    background: var(--text-dark);
  }
  .contact-block {
    position: absolute;
    left: 575px;
    top: 66px;
    color: var(--text-dark);
  }
  .person-name {
    font-weight: 700;
    font-size: 26px;
    line-height: 1.1;
    letter-spacing: 0.5px;
  }
  .person-role {
    font-weight: 400;
    font-size: 19px;
    margin-bottom: 20px;
  }
  .contact-list { list-style: none; }
  .contact-item {
    display: flex;
    align-items: center;
    gap: 10px;
    font-size: 18px;
    line-height: 30px;
  }
  .contact-icon { width: 14px; height: 14px; flex: none; }
  .services {
    position: absolute;
    left: 58px;
    top: 410px;
    color: var(--card-white);
    font-weight: 300;
    font-size: 22px;
    letter-spacing: 0.3px;
  }
</style>
</head>
<body>
  <section class="business-card">
    <svg class="wave-band" viewBox="0 0 880 500" aria-hidden="true">
      <defs>
        <linearGradient id="navy-fade" x1="0" y1="0" x2="1" y2="0">
          <stop offset="0" stop-color="var(--navy-light)"/>
          <stop offset="0.55" stop-color="var(--navy)"/>
        </linearGradient>
      </defs>
      <path fill="var(--slate)" d="M200,330 C400,342 520,330 600,298 C700,258 800,258 880,262 V500 H0 V330 Z"/>
      <path fill="url(#navy-fade)" d="M0,300 C150,300 280,360 420,352 C540,346 600,322 660,302 C740,276 820,284 880,290 V500 H0 Z"/>
    </svg>

    <div class="brand">
      <span class="brand-name">PLM</span>
      <span class="brand-firm">Cabinet Perrin Laval &amp; Mercier</span>
    </div>

    <div class="divider"></div>

    <div class="contact-block">
      <h1 class="person-name">ALEX MOREAU</h1>
      <p class="person-role">Director</p>
      <ul class="contact-list">
        <li class="contact-item">
          <svg class="contact-icon" viewBox="0 0 16 16"><path fill="var(--slate)" d="M4 1 L6.5 4 L5 6 C6 8.5 7.5 10 10 11 L12 9.5 L15 12 L13 15 C7 14.5 1.5 9 1 3 Z"/></svg>
          <span>+123 555 0147</span>
        </li>
        <li class="contact-item">
          <svg class="contact-icon" viewBox="0 0 16 16"><rect x="1" y="3" width="14" height="10" fill="var(--slate)"/><path d="M1 3 L8 9 L15 3" fill="none" stroke="#fff" stroke-width="1.4"/></svg>
          <span>alexmoreau@mail.com</span>
        </li>
        <li class="contact-item">
          <svg class="contact-icon" viewBox="0 0 16 16"><circle cx="8" cy="6" r="4.2" fill="none" stroke="var(--slate)" stroke-width="2"/><path d="M8 10 V15.5" stroke="var(--slate)" stroke-width="2"/></svg>
          <span>www.plm-conseil.com</span>
        </li>
      </ul>
    </div>

    <p class="services">Expertise-comptable · Audit · Conseil</p>
  </section>
</body>
</html>
```